Outdoor mass notification company needing business card design.

Our company name is Harrowgate Signal Systems Inc located in Amory Mississippi and we sell and maintain "Brantor" Mass Notification Sirens in the US. Outdoor sirens notify people of certain severe dangers such as tornados, severe thunderstorms, flooding, hurricanes and tsunamis. We also serve the oil and gas refining industries to warn of Chemical releases, fires, and lightning alerts.

Contact Information for Business Card

Name, title, cell number, email address

Requirements
Nice to have
• The Brantor logo and also the Mildvane logo.

```html
<!DOCTYPE html>
<html lang="en">
<head>
<meta charset="utf-8">
<title>Harrowgate Signal Systems – Business Card</title>
<link href="https://fonts.googleapis.com/css2?family=Lato:wght@400;700&display=swap" rel="stylesheet">
<style>
  :root {
    --stage: #3a3a3a;
    --card: #ffffff;
    --brand-blue: #2f4f6f;
    --band-blue: #3a5775;
    --rule-grey: #8a8a8a;
    --text-grey: #6b6b6b;
    --siren-dark: #1c1c1c;
    --siren-mid: #4a4a4a;
  }
  * { margin: 0; padding: 0; box-sizing: border-box; }
  html, body {
    width: 1200px; height: 875px; overflow: hidden;
    background: var(--stage);
    font-family: "Lato", sans-serif;
  }
  .stage {
    width: 1200px; height: 875px;
    display: flex; align-items: center; justify-content: center; gap: 40px;
  }
  .card {
    position: relative;
    width: 540px; height: 310px;
    background: var(--card);
    border-radius: 18px;
    overflow: hidden;
    box-shadow: 0 14px 30px rgba(0,0,0,.45);
  }
  .wordmark {
    display: flex; align-items: center; gap: 10px;
    color: var(--brand-blue);
    font-weight: 700;
    text-transform: uppercase;
    line-height: 1.05;
  }
  .wordmark .mark {
    width: 14px; height: 14px; border-radius: 50%;
    background: var(--brand-blue); flex: none;
  }
  /* Front */
  .card-front .wordmark {
    position: absolute; top: 34px; right: 36px;
    font-size: 24px; letter-spacing: .5px;
  }
  .siren-photo {
    position: absolute; left: 40px; right: 20px; bottom: 30px; height: 180px;
    background: linear-gradient(180deg, var(--siren-dark) 0%, var(--siren-mid) 75%, #ffffff 100%);
    clip-path: polygon(0 40%, 100% 0, 100% 100%, 0 100%);
    border-radius: 4px;
  }
  /* Back */
  .card-back .wordmark {
    position: absolute; left: 40px; top: 118px;
    font-size: 19px; letter-spacing: .4px; width: 230px;
  }
  .divider {
    position: absolute; left: 300px; top: 38px;
    width: 1.5px; height: 200px; background: var(--brand-blue);
  }
  .contact {
    position: absolute; left: 322px; top: 40px;
    color: var(--text-grey); font-size: 11.5px; line-height: 1.45;
  }
  .contact .name {
    color: var(--brand-blue); font-weight: 700; font-size: 21px;
    text-transform: uppercase; line-height: 1.1;
  }
  .contact .title { margin-bottom: 8px; }
  .contact .address { margin-bottom: 8px; }
  .contact-list { list-style: none; }
  .contact-list li { display: flex; align-items: center; gap: 8px; }
  .contact-list svg { width: 10px; height: 10px; fill: var(--brand-blue); flex: none; }
  .base-rule {
    position: absolute; left: 0; right: 0; bottom: 22px;
    height: 2px; background: var(--rule-grey);
  }
  .base-band {
    position: absolute; left: 0; right: 0; bottom: 0;
    height: 16px; background: var(--band-blue);
  }
</style>
</head>
<body>
<main class="stage">
  <section class="card card-front">
    <div class="wordmark"><span class="mark"></span><span>Harrowgate<br>Signal Systems</span></div>
    <div class="siren-photo" role="img" aria-label="Photograph of a row of outdoor mass notification sirens on poles, rising in height from right to left"></div>
  </section>

  <section class="card card-back">
    <div class="wordmark"><span class="mark"></span><span>Harrowgate<br>Signal Systems</span></div>
    <div class="divider"></div>
    <div class="contact">
      <p class="name">Daniel Reeve</p>
      <p class="title">Founder &amp; CEO</p>
      <p class="address">4120 Cedar Ridge Road<br>Amory, MS 38821</p>
      <ul class="contact-list">
        <li><svg viewBox="0 0 10 10"><path d="M2 0.5 L4 2.5 L3 3.8 Q4.5 6 6.2 7 L7.5 6 L9.5 8 L8 9.5 Q3 9 0.5 2 Z"/></svg>(555) 014-2290</li>
        <li><svg viewBox="0 0 10 10"><path d="M2.5 0 H7.5 V10 H2.5 Z M3.3 1 V8 H6.7 V1 Z"/></svg>(555) 014-2291</li>
        <li><svg viewBox="0 0 10 10"><path d="M2.5 0 H7.5 V3 H9.5 V8 H0.5 V3 H2.5 Z M3.3 0.8 V3 H6.7 V0.8 Z M2.5 6 V10 H7.5 V6 Z"/></svg>(555) 014-2292</li>
        <li><svg viewBox="0 0 10 10"><path d="M0.5 2 H9.5 V8 H0.5 Z M1.2 2.6 L5 5.4 L8.8 2.6 Z"/></svg>info@harrowgatesignal.com</li>
        <li><svg viewBox="0 0 10 10"><circle cx="5" cy="5" r="4.5"/></svg>harrowgatesignal.com</li>
      </ul>
    </div>
    <div class="base-rule"></div>
    <div class="base-band"></div>
  </section>
</main>
</body>
</html>
```